Business Card Design Project

I require a business card for a new coaching business based in Melbourne with global clients. Both companies and individuals will retain our coaching services.

Target Market(s)

Both small business and large corporate in western speaking countries. Individuals requiring support and direction on issues such as fears, phobias, career, relationships, confidence, self esteem etc.

Industry/Entity Type

Business

Font styles to use
Sans Serif

Colors

Designer to choose colors to be used in the design.

Requirements
Must have
• White background to enhance the colours in the logo. Logo on the left.
Should not have
• The black and white version of the logo. Keep the colours.

```html
<!DOCTYPE html>
<html lang="en">
<head>
<meta charset="utf-8">
<title>Clear Horizon Coaching – Business Card</title>
<link href="https://fonts.googleapis.com/css2?family=Arimo:wght@400;700&display=swap" rel="stylesheet">
<style>
  :root {
    --paper: #ffffff;
    --ink: #111111;
    --brand-grey: #6b6d70;
    --brand-dot: #2bb3c9;
    --link: #1a5fc4;
    --wave-pale: #dff5fb;
    --wave-light: #a6e6f5;
    --wave-cyan: #34c6e6;
    --wave-blue: #1a8fd6;
    --wave-navy: #0a4a9e;
  }
  html, body {
    margin: 0;
    padding: 0;
    overflow: hidden;
    background: var(--paper);
  }
  .card {
    position: relative;
    width: 1200px;
    height: 686px;
    overflow: hidden;
    background: var(--paper);
    font-family: "Arimo", Arial, sans-serif;
    color: var(--ink);
  }
  .card__backdrop {
    position: absolute;
    left: 0;
    right: 0;
    top: 250px;
    bottom: 0;
    background: linear-gradient(
      to bottom,
      rgba(255, 255, 255, 0) 0%,
      var(--wave-pale) 22%,
      var(--wave-light) 42%,
      var(--wave-cyan) 62%,
      var(--wave-blue) 80%,
      var(--wave-navy) 100%
    );
  }
  .brand {
    position: absolute;
    left: 80px;
    top: 36px;
    display: flex;
    align-items: center;
    gap: 20px;
  }
  .brand__dot {
    width: 100px;
    height: 100px;
    border-radius: 50%;
    background: var(--brand-dot);
  }
  .brand__name {
    font-weight: 700;
    font-size: 30px;
    line-height: 1.02;
    color: var(--brand-grey);
    text-transform: uppercase;
  }
  .person {
    position: absolute;
    left: 507px;
    top: 182px;
  }
  .person__name,
  .person__role {
    margin: 0;
    font-weight: 400;
    font-size: 35px;
    line-height: 46px;
  }
  .contact {
    margin-top: 14px;
    display: grid;
    grid-template-columns: 172px auto;
    font-size: 31px;
    line-height: 45px;
  }
  .contact__label,
  .contact__value {
    margin: 0;
  }
  .contact__email {
    color: var(--link);
    text-decoration: underline;
  }
</style>
</head>
<body>
  <div class="card">
    <div class="card__backdrop" role="img" aria-label="Flowing blue wave backdrop fading from white to deep ocean blue"></div>

    <div class="brand">
      <span class="brand__dot"></span>
      <span class="brand__name">Clear<br>Horizon<br>Coaching</span>
    </div>

    <div class="person">
      <h1 class="person__name">Maren Holloway-Price</h1>
      <p class="person__role">Performance Consultant and Coach</p>
      <div class="contact">
        <p class="contact__label">Phone</p>
        <p class="contact__value">+61 (0) 400 555 019</p>
        <p class="contact__label">Email</p>
        <p class="contact__value"><span class="contact__email">maren.h@example.com</span></p>
        <p class="contact__label">ABN</p>
        <p class="contact__value">10293847561</p>
      </div>
    </div>
  </div>
</body>
</html>
```